Webdesign für Hersteller für Pack- und Palettieranlagen für den Getränke- und Lebensmittelbereich
Webdesign für Hersteller für Pack- und Palettieranlagen für den Getränke- und Lebensmittelbere..
Zielgruppe
Hersteller für Pack- und Palettieranlagen für den Getränke- und Lebensmittelbereich
Zielgruppe: Getränke- und Lebensmittelhersteller
Aufgabenstellung
die zukünftige Seite soll dynamischer und intuitiver werden
klare Strukturen, aber morderner als das jetztige Layout
Keine Kopie der alten Seite www.kolvand.de!
Startseite soll aufgeräumter sein
Logo, Rufnummer, Mail, Social Media
Startseite mit großem Headerbild (Slider)

```html
<!DOCTYPE html>
<html lang="de">
<head>
<meta charset="utf-8">
<title>KOLVAND Maschinenbau GmbH</title>
<link href="https://fonts.googleapis.com/css2?family=Julius+Sans+One&family=Questrial&display=swap" rel="stylesheet">
<style>
:root{
  --green:#6cb42a;
  --orange:#f58220;
  --dark:#3b3b3b;
  --grey-bg:#d9d9d9;
  --text:#333;
  --muted:#6a6a6a;
  --white:#fff;
  --line:#e4e8ec;
}
*{margin:0;padding:0;box-sizing:border-box}
html,body{width:1200px;height:2570px;overflow:hidden;background:var(--white)}
body{position:relative;font-family:'Questrial',sans-serif;color:var(--text)}
.abs{position:absolute}
.display{font-family:'Julius Sans One',sans-serif;line-height:1;white-space:nowrap}
.brand{left:0;width:1200px;top:44px;display:flex;justify-content:center;align-items:center;gap:8px}
.brand-dot{width:26px;height:26px;border-radius:50%;background:var(--green)}
.brand-name{font-family:'Questrial',sans-serif;font-size:30px;color:var(--green);letter-spacing:1px}
.nav{left:0;width:1200px;display:flex;justify-content:center}
.nav a{font-family:'Julius Sans One',sans-serif;color:var(--text);text-decoration:none;line-height:1}
.nav-main{top:124px;gap:84px}
.nav-main a{font-size:21px}
.nav-sub{top:178px;gap:84px}
.nav-sub a{font-size:16px}
.hero{left:43px;top:227px;width:1123px;height:457px;border-radius:6px;
  background:linear-gradient(90deg,#5a4030 0%,#3e7a8a 25%,#2a6fa8 45%,#d8cfc6 60%,#c9bfb4 75%,#3a6e9e 90%,#4a3a2e 100%)}
.products{left:0;top:727px;width:1200px;height:363px;background:var(--green);color:var(--white)}
.products h2{position:absolute;left:48px;top:44px;font-size:40px;font-weight:400;color:var(--white)}
.products .lead{position:absolute;left:60px;top:92px;font-size:17px;color:var(--white)}
.card{position:absolute;top:154px;width:121px}
.card .thumb{width:121px;height:121px;border-radius:4px}
.card .title{font-size:16px;margin-top:11px;line-height:1}
.card .desc{font-size:12px;margin-top:9px;line-height:1}
.news h2{left:56px;top:1252px;font-size:40px;font-weight:400}
.news p{left:56px;top:1308px;width:430px;font-size:20px;line-height:30px;color:var(--muted)}
.btn{background:var(--dark);color:var(--white);border-radius:6px;font-size:13px;display:flex;align-items:center;justify-content:center}
.news .btn{left:56px;top:1394px;width:81px;height:42px}
.divider{left:520px;top:1215px;width:4px;height:233px;background:var(--orange);border-radius:2px}
.jobs{left:577px;top:1132px;width:599px;height:420px;border-radius:6px;
  background:linear-gradient(110deg,#3f7a23 0%,#5fa33a 45%,#7cbc55 70%,#8fc563 100%);color:var(--white);text-align:center}
.jobs h2{position:absolute;left:0;width:599px;top:165px;font-size:52px;font-weight:400;line-height:58px;white-space:normal}
.jobs p{position:absolute;left:0;width:599px;top:298px;font-size:20px}
.jobs .btn{position:absolute;left:229px;top:350px;width:146px;height:42px;font-size:14px;font-weight:700}
.company{left:0;top:1599px;width:930px;height:386px;background:var(--grey-bg)}
.company h2{position:absolute;left:210px;top:90px;font-size:42px;font-weight:400}
.company p{position:absolute;left:209px;top:142px;width:430px;font-size:20px;line-height:30px;color:var(--muted)}
.company .btn{position:absolute;top:304px;width:68px;height:33px}
.accent{left:618px;top:2002px;width:582px;height:45px;background:var(--orange)}
.contact{left:2px;top:2021px;width:1198px;height:247px;background:var(--green);color:var(--white)}
.contact svg{position:absolute;left:74px;top:35px}
.contact h2{position:absolute;left:143px;top:36px;font-size:40px;font-weight:400}
.contact .col{position:absolute;top:112px;font-size:19px;line-height:30px}
.footer-rule{left:68px;top:2327px;width:1075px;height:1px;background:var(--line)}
.footer-name{left:70px;top:2368px;font-size:20px}
.footer-col{position:absolute;top:2371px;font-family:'Julius Sans One',sans-serif;line-height:1}
.footer-col .topic{font-size:14px;color:var(--text)}
.footer-col .page{font-size:13px;color:var(--muted);margin-top:26px}
.social{left:78px;top:2484px;display:flex;gap:24px}
.social span{width:16px;height:16px;border-radius:50%;background:#666}
</style>
</head>
<body>
<header>
  <div class="abs brand"><span class="brand-dot"></span><span class="brand-name">KOLVAND</span></div>
  <nav class="abs nav nav-main"><a href="#">Unternehmen</a><a href="#">Jobs / Karriere</a><a href="#">Aktuelles</a></nav>
  <nav class="abs nav nav-sub"><a href="#">Palettiertechnik</a><a href="#">Packertechnik</a><a href="#">Fördertechnik</a><a href="#">Anlagen</a><a href="#">Gebrauchtmaschinen</a></nav>
</header>

<div class="abs hero" role="img" aria-label="Headerbild: Industriehalle mit farbigen Rohrleitungen und drei großen weißen Lüftungsrohren"></div>

<section class="abs products">
  <h2 class="display">Produkte</h2>
  <p class="display lead">Erfahren Sie mehr über unsere Produkte. Wählen Sie eine Kategorie:</p>
  <div class="card" style="left:137px"><div class="thumb" role="img" aria-label="Palettieranlage in gelb" style="background:linear-gradient(135deg,#8a8f96,#d8c23a,#6d7177)"></div><div class="title">Title</div><div class="desc">Description</div></div>
  <div class="card" style="left:408px"><div class="thumb" role="img" aria-label="Packanlage mit gelben Gebinden" style="background:linear-gradient(160deg,#b7bcc0,#7f9a7a,#e3c93a)"></div><div class="title">Title</div><div class="desc">Description</div></div>
  <div class="card" style="left:679px"><div class="thumb" role="img" aria-label="Förderband mit Flaschen" style="background:linear-gradient(160deg,#c5c9cc,#7a6a66,#4a2f2a)"></div><div class="title">Title</div><div class="desc">Description</div></div>
  <div class="card" style="left:950px"><div class="thumb" role="img" aria-label="Anlage mit Fässern und Kartons" style="background:linear-gradient(160deg,#a9aeb2,#8a6d4d,#2a2a2a)"></div><div class="title">Title</div><div class="desc">Description</div></div>
</section>

<section class="news">
  <h2 class="abs display">Aktuelles</h2>
  <p class="abs">Another subheading—maybe it’s related to the image on the left, or the button below</p>
  <a class="abs btn">Button</a>
</section>
<div class="abs divider"></div>

<section class="abs jobs" role="img" aria-label="Mitarbeiter an einem Motorblock, grün eingefärbt">
  <h2 class="display">Jobs &amp;<br>Karriere</h2>
  <p>Werden Sie Teil unseres Teams.</p>
  <a class="btn">Jetzt bewerben.</a>
</section>

<section class="abs company">
  <h2 class="display">Unternehmen</h2>
  <p>Body text for whatever you’d like to suggest. Add main takeaway points, quotes, anecdotes, or even a very very short story.</p>
  <a class="btn" style="left:390px">Button</a>
  <a class="btn" style="left:498px">Button</a>
  <a class="btn" style="left:606px">Button</a>
  <a class="btn" style="left:714px">Button</a>
</section>

<div class="abs accent"></div>
<section class="abs contact">
  <svg width="42" height="42" viewBox="0 0 42 42" fill="none" stroke="#fff" stroke-width="3"><circle cx="21" cy="21" r="19"/><circle cx="21" cy="17" r="6"/><path d="M9 34c3-6 7-8 12-8s9 2 12 8"/></svg>
  <h2 class="display">Kontakt</h2>
  <div class="col" style="left:168px">KOLVAND Maschinenbau GmbH<br>Am Lindenweg 12<br>01234 Talheim</div>
  <div class="col" style="left:543px;top:114px">Telefon: 030123 / 456 - 0<br>Fax: 030123 / 456 - 14<br>E-Mail: info@kolvand.de</div>
</section>

<footer>
  <div class="abs footer-rule"></div>
  <div class="abs display footer-name">KOLVAND Maschinenbau GmbH</div>
  <div class="footer-col" style="left:620px"><div class="topic">Topic</div><div class="page">Page</div><div class="page">Page</div><div class="page">Page</div></div>
  <div class="footer-col" style="left:803px"><div class="topic">Topic</div><div class="page">Page</div><div class="page">Page</div><div class="page">Page</div></div>
  <div class="footer-col" style="left:986px"><div class="topic">Topic</div><div class="page">Page</div><div class="page">Page</div><div class="page">Page</div></div>
  <div class="abs social"><span></span><span></span><span></span><span></span></div>
</footer>
</body>
</html>
```